Hörbuchcover
Zielgruppe
Spiritueller Hörbuchverlag für ganzheitliche Gesundheit, Glück und Wohlstand.
Aufgabenstellung
Benötigt wird ein schönes quadratisches Cover, 2400x2400 mindestens 72dpi für ein Hörbuchcover.
Auf dem Cover soll eine gelb/orange Rose zu in Form einer Blüte zu sehen sein.
Titel: Innere Wandlung
Untertitel: Emotionen sind der Schlüssel für Gesundheit, Energie & Lebensfreude
Autorenname: Dr. med. Birgit Wolkenstein
Das Feloria Logo soll unten mittig sitzen.
Es folgen weiterer Hörbücher von dieser Autorin und es wäre gut wenn man die folgenden Cover in einem ähnlichen Stil halten könnte. Ein harmonisches und gut zu erkennendes Design mit hohem Wiedererkennungseffekt. Ich freue mich auf kreative Designvorschläge.
Auf feloria.de kann man sehen wo das Logo sitzen soll.
Herzliche Grüße - Jens

```html
<!DOCTYPE html>
<html lang="de">
<head>
<meta charset="utf-8">
<title>Innere Wandlung – Hörbuchcover</title>
<link rel="stylesheet" href="https://fonts.googleapis.com/css2?family=Courgette&family=Montserrat:wght@400&family=Overpass:wght@400;600&display=swap">
<style>
  :root {
    --sun-top: #ffce64;
    --sun-mid: #ffb03f;
    --sun-low: #ffab37;
    --band: rgba(250, 138, 8, 0.55);
    --ink: #333333;
    --paper: #ffffff;
  }
  html, body {
    margin: 0;
    padding: 0;
    overflow: hidden;
    background: var(--sun-low);
  }
  .cover {
    position: relative;
    width: 1200px;
    height: 1200px;
    overflow: hidden;
    background: linear-gradient(180deg, var(--sun-top) 0px, var(--sun-top) 320px, var(--sun-mid) 380px, var(--sun-low) 1200px);
    font-family: "Overpass", sans-serif;
    color: var(--ink);
  }
  .bloom, .title-caps {
    position: absolute;
    inset: 0;
    width: 1200px;
    height: 1200px;
  }
  .title-caps text {
    font-family: "Montserrat", sans-serif;
    font-weight: 400;
    font-size: 228px;
    fill: var(--paper);
  }
  .title-script {
    position: absolute;
    top: 30px;
    left: 0;
    width: 1200px;
    text-align: center;
    font-family: "Courgette", cursive;
    font-weight: 400;
    font-size: 128px;
    line-height: 1;
    color: var(--ink);
    margin: 0;
  }
  .author {
    position: absolute;
    top: 388px;
    left: 0;
    width: 1200px;
    text-align: center;
    font-size: 39px;
    letter-spacing: 2px;
    line-height: 1;
    margin: 0;
  }
  .subtitle {
    position: absolute;
    top: 828px;
    left: 0;
    width: 1200px;
    text-align: center;
    font-size: 58px;
    line-height: 70px;
    margin: 0;
  }
  .publisher {
    position: absolute;
    top: 1100px;
    left: 0;
    width: 1200px;
    display: flex;
    justify-content: center;
    align-items: center;
    gap: 16px;
    font-weight: 600;
    font-size: 40px;
    letter-spacing: 6px;
    color: #111111;
  }
  .publisher .dot {
    width: 22px;
    height: 22px;
    border-radius: 50%;
    background: #111111;
  }
</style>
</head>
<body>
<div class="cover">
  <svg class="bloom" viewBox="0 0 1200 1200">
    <defs>
      <radialGradient id="bloomFill" cx="50%" cy="40%" r="60%">
        <stop offset="0%" stop-color="#ffffff"/>
        <stop offset="70%" stop-color="#fff6e6"/>
        <stop offset="100%" stop-color="#ffd79a"/>
      </radialGradient>
    </defs>
    <path role="img" aria-label="Stilisierte gelb-orange Rosenblüte auf hellem Grund"
          d="M600 433 C 760 433 880 500 960 610 C 1010 700 1020 790 1015 860 C 1005 1000 930 1100 780 1200 L 415 1200 C 270 1100 190 1000 182 860 C 178 760 200 680 250 610 C 330 500 440 433 600 433 Z"
          fill="url(#bloomFill)"/>
    <rect class="tagline-band" x="0" y="807" width="1200" height="184" fill="var(--band)"/>
  </svg>

  <h1 class="title-script">innere</h1>
  <svg class="title-caps" viewBox="0 0 1200 1200" role="heading" aria-level="2" aria-label="Wandlung">
    <text x="122" y="369" textLength="952" lengthAdjust="spacingAndGlyphs">WANDLUNG</text>
  </svg>
  <p class="author">Dr. med. Birgit Wolkenstein</p>

  <p class="subtitle">Emotionen sind der Schlüssel für<br>Gesundheit, Energie &amp; Lebensfreude</p>

  <div class="publisher"><span class="dot"></span><span>FELORIA</span></div>
</div>
</body>
</html>
```